**URGENT // ENVIRONMENTAL // QUICK TURN AROUND**

We are looking for an A-Grade designer to work with longterm, starting with the successful design for our website & logo; Kestrel Hub.

Kestrel Hub is a business that focusses on grouping environmentally conscious people together and helping them get "bulk buy" discounts by purchasing large volumes together; solar, energy efficency, wind turbines, and the like.

The Logo and website must have a green feel, as we are here to protect the environment, whilst also helping our customers save money.

The website must also have a blog feature, allowing us to post and keep people up to date with the latest in the industry.

Target Market(s)

FAMILIES WITHIN REGIONAL AUSTRALIA WANTING TO EITHER SAVE MONEY ON ELECTRICITY BILLS, OR REDUCE CARBON EMISSIONS.

Industry/Entity Type

Solar Energy

Logo Text

KESTREL HUB

Number of Pages Required

5+ page

Font styles to use
Serif
Sans Serif

Colors

Designer to choose colors to be used in the design.

Requirements
Must have
• 1.HOME PAGE
• 2.OUR SERVICES PAGE
• - RENEWABLE ENERGY
• - LIGHTING SYSTEMS
• - ENERGY ASSESSMENT
• - R.H.L.P SCHEME
• - ENERGY COMPARISON
• 4. BOOK AN APPOINTMENT
• 5. IN THE NEWS
• 6. SUBSCRIBE TO NEWSLETTER
• 7. CONTACT US
• MUST LOOK VERY PROFESSIONAL, WITH LOTS OF INFORMATION, IT CANNOT BE BARE AND SIMPLE.
• Can use www.tarnfieldgoodsandwares.com.au which is our other brand for copy and ideas - HOWEVER, THIS IS THE REASON WE ARE RE-BRANDING, AS THIS BRAND HAS COME UNDER FAR TOO MUCH CRITICISM FOR LACK OF INFORMATION AND LOOKING TO SIMPLE.
Nice to have
• BLOG FEATURE
Should not have
• ANYTHING THAT APPEARS NON-ENVIRONMENTALS

```html
<!DOCTYPE html>
<html lang="en">
<head>
<meta charset="utf-8">
<title>Kestrel Hub</title>
<link rel="stylesheet" href="https://fonts.googleapis.com/css2?family=Raleway:wght@400;500;600;700&display=swap">
<style>
:root{
  --green:#1aa90d;
  --green-dark:#148a0a;
  --white:#ffffff;
  --ink:#444444;
  --muted:#8a8a8a;
  --sky:#5a8fd6;
}
*{box-sizing:border-box;margin:0;padding:0}
html,body{width:1200px;height:3689px;overflow:hidden}
body{position:relative;font-family:'Raleway',sans-serif;background:var(--white);color:var(--ink)}
.abs{position:absolute}

.site-header{left:0;top:0;width:1200px;height:88px;background:var(--white)}
.brand{left:74px;top:27px;font-size:30px;font-weight:700;color:var(--ink);letter-spacing:.5px}
.brand span{color:var(--green)}
.nav-link{top:38px;font-size:13px;font-weight:600;color:var(--ink);text-transform:uppercase}
.nav-link.active{color:var(--green)}
.btn-book{left:895px;top:25px;width:231px;height:44px;background:var(--green);color:var(--white);font-size:14px;font-weight:700;display:flex;align-items:center;justify-content:center}

.hero{left:0;top:88px;width:1200px;height:472px;background:linear-gradient(180deg,#3f7fd4 0%,#8cb9ea 45%,#4b7fc2 62%,#2f5f9e 80%,#5fae2e 100%)}
.hero-text{left:74px;top:262px;width:560px;font-size:38px;line-height:41px;color:#1d1d1d;font-weight:400}
.hero-dots{left:74px;top:512px;display:flex;gap:8px}
.hero-dots i{width:9px;height:9px;border-radius:50%;background:var(--white);opacity:.7;display:block}
.hero-dots i:first-child{background:var(--green);opacity:1}

.mission{left:0;top:560px;width:1200px;height:222px;background:var(--green);color:var(--white);text-align:center}
.mission h2{position:absolute;left:0;width:1200px;top:44px;font-size:52px;font-weight:400;letter-spacing:1px}
.mission p{position:absolute;left:110px;width:980px;top:118px;font-size:19px;line-height:30px}

.section-title{font-size:60px;line-height:60px;font-weight:400;text-transform:uppercase;color:var(--green)}
.on-green .section-title{color:var(--white);font-size:50px;line-height:52px}
.copy{font-size:17px;line-height:31px;color:var(--muted)}
.on-green .copy{color:var(--white)}
.btn-outline{height:44px;border:2px solid var(--green);color:var(--green);font-size:13px;font-weight:700;display:flex;align-items:center;justify-content:center;text-transform:uppercase;background:var(--white)}
.on-green .btn-outline{border-color:var(--white);color:var(--white);background:transparent}

.photo{display:block}

.band{left:0;width:1200px;background:var(--green)}
.band-solar{top:1180px;height:610px;clip-path:polygon(0 0,100% 99px,100% 100%,0 512px)}
.band-energy{top:2159px;height:571px;clip-path:polygon(0 0,100% 103px,100% 100%,0 467px)}

.blog-title{left:0;width:1200px;top:2815px;text-align:center;font-size:52px;font-weight:400;color:var(--green)}
.post{width:330px}
.post .photo{width:330px;height:197px}
.post h3{margin-top:22px;font-size:16px;font-weight:700;color:var(--green);text-transform:uppercase}
.post .date{margin-top:10px;font-size:12px;font-weight:600;color:var(--ink);display:flex;align-items:center;gap:8px}
.post p{margin-top:10px;font-size:14px;line-height:20px;color:var(--muted)}
.post .btn-outline{margin-top:22px;width:188px}

.site-footer{left:0;top:3344px;width:1200px;height:345px;background:var(--green)}
.footer-scene{left:0;top:3344px;width:1200px;height:197px;background:linear-gradient(180deg,#ffffff 0%,#ffffff 30%,#6cc85f 70%,var(--green) 100%)}
.footer-copy{left:76px;font-size:13px;color:var(--white)}
.follow{left:942px;top:3586px;font-size:13px;font-weight:700;color:var(--white);text-transform:uppercase}
.socials{left:942px;top:3624px;display:flex;gap:20px}
.socials i{display:block;width:18px;height:18px;border-radius:50%;background:var(--white)}
</style>
</head>
<body>

<header class="site-header abs">
  <div class="brand abs"><span>KESTREL</span> HUB</div>
  <nav>
    <a class="nav-link active abs" style="left:548px">Home</a>
    <a class="nav-link abs" style="left:632px">Our Services</a>
    <a class="nav-link abs" style="left:772px">Contact Us</a>
  </nav>
  <div class="btn-book abs">BOOK AN APPOINTMENT</div>
</header>

<section class="hero abs" role="img" aria-label="Solar panels and a wind turbine on green grass under a blue sky"></section>
<p class="hero-text abs">Discover how we can help you create an energy efficient home that saves money.</p>
<div class="hero-dots abs"><i></i><i></i><i></i><i></i><i></i></div>

<section class="mission abs">
  <h2>OUR MISSION</h2>
  <p>Reduce our customers' power bills down and keep them under control into the future. We take great pride in knowing everything about saving money on power so you don't have to!</p>
</section>

<section class="about">
  <h2 class="section-title abs" style="left:74px;top:850px">About Us</h2>
  <p class="copy abs" style="left:74px;top:928px;width:600px">We love power but we love saving it even more! At Tarnfield Power &amp; Lighting we are committed to helping Australian customers connect with leading tier-1 suppliers for Solar, LED and other energy saving products.</p>
  <div class="btn-outline abs" style="left:74px;top:1094px;width:189px">Read More</div>
  <div class="photo abs" style="left:740px;top:782px;width:460px;height:390px;background:radial-gradient(ellipse at 55% 55%,#7dbb45 0%,#c9e2b3 45%,#ffffff 75%)" role="img" aria-label="Hand holding a patch of earth with a tree, solar panel and wind turbines"></div>
</section>

<div class="band band-solar abs"></div>
<section class="on-green">
  <div class="photo abs" style="left:76px;top:1313px;width:433px;height:325px;background:linear-gradient(160deg,#8fb4d8 0%,#c9a877 40%,#2f4f86 75%,#1d3461 100%)" role="img" aria-label="Technician installing solar panels on a roof"></div>
  <h2 class="section-title abs" style="left:548px;top:1306px">Solar<br>Consultations</h2>
  <p class="copy abs" style="left:548px;top:1433px;width:580px">Solar panels are a great way to tap into the free power from our Australian sun! With more usable sunlight than any other country in the world we really do think getting solar is a no brainer!</p>
  <div class="btn-outline abs" style="left:548px;top:1593px;width:187px">Solar Enquiry</div>
</section>

<section class="led">
  <h2 class="section-title abs" style="left:74px;top:1827px;font-size:50px;line-height:52px">LED Lighting<br>Installations</h2>
  <p class="copy abs" style="left:74px;top:1944px;width:560px">LED lighting on average uses 90% less power than halogen globes, last for 20+ years and reduce the risk of house fires. Best of all they are FREE*</p>
  <div class="btn-outline abs" style="left:74px;top:2078px;width:189px">LED Enquiry</div>
  <div class="photo abs" style="left:691px;top:1820px;width:435px;height:319px;background:linear-gradient(135deg,#7fb35a 0%,#c8c8c8 40%,#3a5a8a 75%,#1f3358 100%)" role="img" aria-label="LED light globes resting on a solar panel"></div>
</section>

<div class="band band-energy abs"></div>
<section class="on-green">
  <div class="photo abs" style="left:76px;top:2292px;width:433px;height:322px;background:linear-gradient(180deg,#1f5fa8 0%,#3d87c4 45%,#e5935a 78%,#2a3550 100%)" role="img" aria-label="Wind turbines silhouetted against a sunset sky"></div>
  <h2 class="section-title abs" style="left:548px;top:2284px">Energy<br>Assessments</h2>
  <p class="copy abs" style="left:548px;top:2410px;width:580px">Discover how much energy you could be saving after an energy assessment from one of our highly trained professionals. Simply let us know the best time to contact you and help create a more efficient and comfortable home.</p>
  <div class="btn-outline abs" style="left:548px;top:2572px;width:226px">Energy Assessments</div>
</section>

<h2 class="blog-title abs">BLOG POSTS</h2>
<section class="blog">
  <article class="post abs" style="left:76px;top:2897px">
    <div class="photo" style="background:linear-gradient(135deg,#3f8f2a 0%,#b08a5a 50%,#5aa83a 100%)" role="img" aria-label="Hand holding an energy saving sign and bulb"></div>
    <h3>Vestibulum ante ipsum primis..</h3>
    <div class="date"><svg width="11" height="11" viewBox="0 0 11 11"><rect x="0.5" y="1.5" width="10" height="9" fill="none" stroke="#444"/><rect x="0.5" y="1.5" width="10" height="3" fill="#444"/></svg>APR 06, 2017</div>
    <p>Aenean a nibh eget turpis vehicula tempus ac sed massa. Vestibulum dolor nulla, ultrices ac tincidunt sed, laoreet non est.</p>
    <div class="btn-outline">Read More</div>
  </article>
  <article class="post abs" style="left:435px;top:2897px">
    <div class="photo" style="background:linear-gradient(180deg,#4a8fd0 0%,#9fd0ef 40%,#7ec04a 70%,#3d8a1e 100%)" role="img" aria-label="Light bulb lying in fresh green grass"></div>
    <h3>Vestibulum ante ipsum primis..</h3>
    <div class="date"><svg width="11" height="11" viewBox="0 0 11 11"><rect x="0.5" y="1.5" width="10" height="9" fill="none" stroke="#444"/><rect x="0.5" y="1.5" width="10" height="3" fill="#444"/></svg>APR 06, 2017</div>
    <p>Aenean a nibh eget turpis vehicula tempus ac sed massa. Vestibulum dolor nulla, ultrices ac tincidunt sed, laoreet non est.</p>
    <div class="btn-outline">Read More</div>
  </article>
  <article class="post abs" style="left:797px;top:2897px">
    <div class="photo" style="background:linear-gradient(180deg,#2f6fc4 0%,#a9cbef 55%,#e0d24a 78%,#6aa83a 100%)" role="img" aria-label="Wind turbines above a yellow flower field"></div>
    <h3>Vestibulum ante ipsum primis..</h3>
    <div class="date"><svg width="11" height="11" viewBox="0 0 11 11"><rect x="0.5" y="1.5" width="10" height="9" fill="none" stroke="#444"/><rect x="0.5" y="1.5" width="10" height="3" fill="#444"/></svg>APR 06, 2017</div>
    <p>Aenean a nibh eget turpis vehicula tempus ac sed massa. Vestibulum dolor nulla, ultrices ac tincidunt sed, laoreet non est.</p>
    <div class="btn-outline">Read More</div>
  </article>
</section>

<footer>
  <div class="site-footer abs"></div>
  <div class="footer-scene abs" role="img" aria-label="Green silhouette landscape of trees, houses and wind turbines"></div>
  <p class="footer-copy abs" style="top:3592px">Copyright © 2017 Company Name All Right Reserved</p>
  <p class="footer-copy abs" style="top:3627px">ABN - 51 824 306 179</p>
  <p class="follow abs">Follow Us</p>
  <div class="socials abs"><i></i><i></i><i></i><i></i><i></i></div>
</footer>

</body>
</html>
```